Real eatate

My company name is “Maple Crest Realestate” i would like to create a business card. I would like something modern and sleek similar to picture uploaded. All text in the business card should be black and the logo gold any shade.

```html
<!DOCTYPE html>
<html lang="en">
<head>
<meta charset="utf-8">
<title>Maple Crest Realestate – Business Card</title>
<link rel="stylesheet" href="https://fonts.googleapis.com/css2?family=Montserrat:wght@400;500;600&display=swap">
<style>
  :root {
    --page-bg: #f3f3f3;
    --card-dark: #000000;
    --card-light: #ececec;
    --ink: #111111;
    --ink-light: #ffffff;
    --gold: #c9a560;
    --gold-edge: #d8c08a;
  }
  * { box-sizing: border-box; margin: 0; padding: 0; }
  html, body {
    width: 1200px;
    height: 1200px;
    overflow: hidden;
    background: var(--page-bg);
    font-family: "Montserrat", sans-serif;
  }
  .sheet {
    width: 1200px;
    height: 1200px;
    display: flex;
    flex-direction: column;
    align-items: center;
    justify-content: center;
    gap: 64px;
  }
  .card {
    width: 760px;
    height: 434px;
    position: relative;
    border-bottom: 2px solid var(--gold-edge);
    border-right: 2px solid var(--gold-edge);
    box-shadow: 0 10px 24px rgba(0, 0, 0, 0.12);
  }
  .card--front {
    background: var(--card-dark);
    display: flex;
    align-items: center;
    justify-content: center;
  }
  .brand {
    display: flex;
    align-items: center;
    gap: 16px;
  }
  .brand__dot {
    width: 30px;
    height: 30px;
    border-radius: 50%;
    background: var(--gold);
  }
  .brand__name {
    color: var(--ink-light);
    font-weight: 500;
    font-size: 34px;
    letter-spacing: 0.5px;
  }
  .card--back {
    background: var(--card-light);
    color: var(--ink);
  }
  .holder {
    position: absolute;
    left: 56px;
    bottom: 52px;
  }
  .holder__name {
    font-weight: 600;
    font-size: 30px;
    letter-spacing: 0.3px;
  }
  .holder__role {
    margin-top: 2px;
    font-weight: 600;
    font-size: 11px;
    letter-spacing: 2.4px;
    text-transform: uppercase;
  }
  .contact {
    position: absolute;
    right: 56px;
    top: 64px;
    font-size: 13.5px;
    line-height: 1.38;
    letter-spacing: 1.6px;
    font-weight: 400;
  }
  .contact__address { margin-bottom: 14px; }
  .contact__label { font-weight: 600; display: inline-block; width: 26px; }
</style>
</head>
<body>
  <main class="sheet">
    <section class="card card--front" aria-label="Card front">
      <div class="brand">
        <span class="brand__dot"></span>
        <span class="brand__name">Maple Crest Realestate</span>
      </div>
    </section>

    <section class="card card--back" aria-label="Card back">
      <address class="contact" style="font-style: normal;">
        <p class="contact__address">2718 Linden Hollow Road<br>Fair Oaks, TX 40351<br>Austin</p>
        <p><span class="contact__label">T:</span>512.555.0147</p>
        <p><span class="contact__label">M:</span>512.555.0193</p>
        <p><span class="contact__label">E:</span>daniel@maplecrest.com</p>
        <p><span class="contact__label">W:</span>maplecrest.com</p>
      </address>
      <div class="holder">
        <p class="holder__name">Daniel R. Hayes</p>
        <p class="holder__role">Business Manager</p>
      </div>
    </section>
  </main>
</body>
</html>
```